Bref créative
Overseas Capital Partners
I need single sided standard sized Business Card [3.5" x 2"]
May be same as in logo, may be another
Professional
Marek Dobrzyn
Manager
ul. Lipowa 17
41-806 Katowice
Poland
marek.dobrzyn@korvant.com.pl
www.korvant.com.pl

```html
<!DOCTYPE html>
<html lang="en">
<head>
<meta charset="utf-8">
<title>Korvant – Business Card Designs</title>
<link rel="stylesheet" href="https://fonts.googleapis.com/css2?family=Open+Sans:wght@400;600;700&display=swap">
<style>
  :root {
    --stage: #e9ecef;
    --card-white: #ffffff;
    --card-mist: #eceff2;
    --sky-deep: #1aa3df;
    --sky-light: #74d2f4;
    --navy: #1c3550;
    --ink: #3b3f44;
    --ink-soft: #5f666d;
    --brand: #2aa9e0;
  }
  * { box-sizing: border-box; margin: 0; padding: 0; }
  html, body { width: 1200px; height: 792px; overflow: hidden; }
  body {
    background: var(--stage);
    font-family: "Open Sans", Arial, sans-serif;
    position: relative;
  }
  .icon-defs { position: absolute; width: 0; height: 0; }

  .card {
    position: absolute;
    width: 500px;
    height: 286px;
    border-radius: 22px;
    overflow: hidden;
    background: linear-gradient(180deg, var(--card-white) 0%, var(--card-mist) 100%);
    box-shadow: 0 2px 6px rgba(0,0,0,.12);
  }
  .card--top { left: 460px; top: 50px; }
  .card--left { left: 60px; top: 380px; }
  .card--right { left: 620px; top: 420px; }

  .header-band {
    position: absolute; left: 0; top: 0; width: 100%; height: 100px;
    background: linear-gradient(90deg, var(--sky-deep) 0%, var(--sky-light) 100%);
  }
  .card--left .header-band { background: linear-gradient(90deg, var(--sky-light) 0%, var(--sky-deep) 100%); }
  .card--right .header-band { height: 110px; }

  .person { position: absolute; }
  .person__name { font-size: 22px; font-weight: 700; color: var(--navy); line-height: 1.1; white-space: nowrap; }
  .person__role { font-size: 15px; font-weight: 400; color: #fff; margin-top: 4px; }
  .person--on-white .person__name { font-size: 18px; }
  .person--on-white .person__role { font-size: 13px; color: var(--ink-soft); }

  .contacts { position: absolute; list-style: none; }
  .contacts li { display: flex; align-items: center; gap: 7px; font-size: 10px; color: var(--ink); line-height: 17px; white-space: nowrap; }
  .contacts svg { width: 11px; height: 11px; fill: var(--brand); flex: none; }

  .office { position: absolute; font-size: 10px; color: var(--ink); line-height: 15px; white-space: nowrap; }
  .office__company { font-weight: 700; }

  .brand-lockup {
    position: absolute;
    display: flex; flex-direction: column; align-items: center; gap: 10px;
  }
  .brand-lockup__square { width: 40px; height: 40px; background: var(--brand); border-radius: 4px; }
  .brand-lockup__name { font-size: 28px; font-weight: 600; color: var(--brand); line-height: 1; }

  .arch { position: absolute; left: 200px; top: 38px; width: 100px; height: 72px; }
</style>
</head>
<body>

<svg class="icon-defs" aria-hidden="true">
  <symbol id="icon-phone" viewBox="0 0 12 12"><rect x="3" y="0.5" width="6" height="11" rx="1.2"/><rect x="4" y="2" width="4" height="6.5" fill="#fff"/></symbol>
  <symbol id="icon-mail" viewBox="0 0 12 12"><rect x="0.5" y="2.5" width="11" height="7.5" rx="1"/><path d="M1 3 L6 7 L11 3" stroke="#fff" stroke-width="1" fill="none"/></symbol>
  <symbol id="icon-web" viewBox="0 0 12 12"><circle cx="6" cy="6" r="5.5"/><path d="M0.5 6 H11.5 M6 0.5 C3 3.5 3 8.5 6 11.5 M6 0.5 C9 3.5 9 8.5 6 11.5" stroke="#fff" stroke-width=".8" fill="none"/></symbol>
</svg>

<!-- Card variant: header band with name, brand right of contacts -->
<article class="card card--top">
  <div class="header-band"></div>
  <div class="person" style="left:34px; top:32px;">
    <p class="person__name">Marek Dobrzyn</p>
    <p class="person__role">Manager</p>
  </div>
  <ul class="contacts" style="left:34px; top:118px;">
    <li><svg><use href="#icon-phone"/></svg>+48 602 71 43 18</li>
    <li><svg><use href="#icon-mail"/></svg>marek.dobrzyn@korvant.com.pl</li>
    <li><svg><use href="#icon-web"/></svg>www.korvant.com.pl</li>
  </ul>
  <div class="brand-lockup" style="left:250px; top:130px; width:200px;">
    <div class="brand-lockup__square"></div>
    <p class="brand-lockup__name">Korvant</p>
  </div>
  <div class="office" style="left:34px; top:220px;">
    <p class="office__company">Overseas Capital Partners</p>
    <p>ul. Lipowa 17</p>
    <p>41-806 Katowice, Poland</p>
  </div>
</article>

<!-- Card variant: brand left, contacts right -->
<article class="card card--left">
  <div class="header-band"></div>
  <div class="person" style="left:230px; top:32px;">
    <p class="person__name">Marek Dobrzyn</p>
    <p class="person__role">Manager</p>
  </div>
  <div class="brand-lockup" style="left:20px; top:122px; width:180px;">
    <div class="brand-lockup__square"></div>
    <p class="brand-lockup__name">Korvant</p>
  </div>
  <ul class="contacts" style="left:230px; top:116px;">
    <li><svg><use href="#icon-phone"/></svg>+48 602 71 43 18</li>
    <li><svg><use href="#icon-mail"/></svg>marek.dobrzyn@korvant.com.pl</li>
    <li><svg><use href="#icon-web"/></svg>www.korvant.com.pl</li>
  </ul>
  <div class="office" style="left:230px; top:188px;">
    <p class="office__company">Overseas Capital Partners</p>
    <p>ul. Lipowa 17</p>
    <p>41-806 Katowice, Poland</p>
  </div>
</article>

<!-- Card variant: arch in band, details in a bottom row -->
<article class="card card--right">
  <div class="header-band"></div>
  <svg class="arch" viewBox="0 0 100 72" aria-hidden="true">
    <path d="M0 72 V42 Q0 0 50 0 Q100 0 100 42 V72 Z" fill="#ffffff"/>
  </svg>
  <div class="brand-lockup" style="left:150px; top:62px; width:200px;">
    <div class="brand-lockup__square"></div>
    <p class="brand-lockup__name">Korvant</p>
  </div>
  <div class="person person--on-white" style="left:26px; top:202px;">
    <p class="person__name">Marek Dobrzyn</p>
    <p class="person__role">Manager</p>
  </div>
  <div class="office" style="left:172px; top:198px;">
    <p class="office__company">Overseas Capital Partners</p>
    <p>ul. Lipowa 17</p>
    <p>41-806 Katowice, Poland</p>
  </div>
  <ul class="contacts" style="left:318px; top:196px;">
    <li><svg><use href="#icon-phone"/></svg>+48 602 71 43 18</li>
    <li><svg><use href="#icon-mail"/></svg>marek.dobrzyn@korvant.com.pl</li>
    <li><svg><use href="#icon-web"/></svg>www.korvant.com.pl</li>
  </ul>
</article>

</body>
</html>
```